Bramble Travel Planners needs an bold logo and business card design

Thanks you all for helping me with this project your assistance is appriciated
I am starting a home based travel agency and I need a bold and eye catching logo and business card designed.
I want to convey a sense of FREEDOM, expertise, customer service for travel customers
Bramble travel planners is a full service travel agency focused on customer service and adding value to a vacation and travel planning.
my idea is for a card that looks like an cruise ship boarding pass or passport with stamps with a back drop of beautiful beach scene, resort hotel and happiness.
The logo should be eye catching, unique but give a sense of freedom and it should be travel related
We want to give customers a sense of Freedom from travel planning, freedom from researching cruises and hotels and freedom to enjoy a wonderful cost effective vacation.

Target Market(s)

Customers considering travel for vacations, family reunions, business and weddings

Industry/Entity Type

Travel Industry

Contact Information for Business Card

Bramble Travel Planners
Warren Pelfrey Owner
WPelfrey@BrambleTravelPlanners.com
BrambleTravelPlanners.com
(555) 014-2287

Logo Text

“One’s destination is never a place, but a new way of seeing things.”

Font styles to use
Serif

Colors
85cae6
0492cd
ec1f27
e667a6
b768aa
33b8a4

Requirements
Must have
• The Logo you create should be on the busoness card
• should be clean, easy to read and attractive
• something you that would make you want to work with a travel agent
Nice to have
• should have cruise ship, hotel on the card or something that conveys travel
Should not have
• Should not have the american flag
• no yellow on the card

```html
<!DOCTYPE html>
<html lang="en">
<head>
<meta charset="utf-8">
<title>Bramble Travel Planners – Business Card</title>
<link rel="stylesheet" href="https://fonts.googleapis.com/css2?family=Exo+2:wght@600&family=Open+Sans:wght@400;700&display=swap">
<style>
  :root {
    --backdrop: #ecebe8;
    --card-white: #ffffff;
    --ocean: #1d7fae;
    --ocean-deep: #135e8e;
    --navy: #0e4a7d;
    --leaf: #8cc63f;
    --text-light: #f2f7fb;
    --shadow: rgba(0, 0, 0, 0.22);
  }
  * { box-sizing: border-box; margin: 0; padding: 0; }
  html, body { width: 1200px; height: 800px; overflow: hidden; }
  body {
    position: relative;
    background: var(--backdrop);
    font-family: "Open Sans", Arial, sans-serif;
  }

  /* Back of card */
  .card-back {
    position: absolute;
    left: 90px; top: 150px;
    width: 320px; height: 540px;
    border-radius: 4px;
    background: linear-gradient(160deg, var(--ocean) 0%, var(--ocean-deep) 100%);
    box-shadow: 0 10px 28px var(--shadow);
    overflow: hidden;
  }
  .card-back__name {
    position: absolute;
    left: 245px; top: 60px;
    transform: rotate(90deg);
    transform-origin: left top;
    font-family: "Exo 2", Arial, sans-serif;
    font-weight: 600;
    font-size: 34px;
    line-height: 1.05;
    color: var(--text-light);
    white-space: nowrap;
  }
  .card-back__mark {
    position: absolute;
    left: 40px; top: 290px;
    width: 230px; height: 230px;
    border-radius: 50%;
    background: rgba(255, 255, 255, 0.07);
  }

  /* Front of card */
  .card-front {
    position: absolute;
    left: 470px; top: 320px;
    width: 640px; height: 366px;
    border-radius: 4px;
    background: var(--card-white);
    box-shadow: 0 10px 28px var(--shadow);
    overflow: hidden;
  }
  .card-front__waves { position: absolute; inset: 0; }
  .card-front__mark {
    position: absolute;
    left: 150px; top: 30px;
    width: 110px; height: 110px;
    border-radius: 50%;
    background: var(--ocean);
  }
  .card-front__name {
    position: absolute;
    right: 36px; top: 140px;
    font-family: "Exo 2", Arial, sans-serif;
    font-weight: 600;
    font-size: 32px;
    line-height: 1.2;
    color: var(--navy);
    white-space: nowrap;
  }
  .contact {
    position: absolute;
    right: 36px; top: 246px;
    text-align: right;
    color: var(--text-light);
    font-size: 15px;
    line-height: 1.35;
  }
  .contact__person {
    font-weight: 700;
    font-size: 19px;
    letter-spacing: 0.5px;
    color: var(--leaf);
    text-transform: uppercase;
  }
  .contact__role { margin-bottom: 4px; }
  .contact__line { display: flex; justify-content: flex-end; align-items: center; gap: 8px; }
  .contact__icon { width: 16px; height: 16px; flex: none; }

  /* Standalone logo */
  .brand-logo {
    position: absolute;
    right: 40px; top: 40px;
    width: 240px;
    display: flex; flex-direction: column; align-items: center; gap: 16px;
  }
  .brand-logo__mark {
    width: 150px; height: 150px;
    border-radius: 50%;
    background: var(--navy);
  }
  .brand-logo__name {
    font-family: "Exo 2", Arial, sans-serif;
    font-weight: 600;
    font-size: 26px;
    color: var(--navy);
    text-align: center;
    line-height: 1.1;
  }
</style>
</head>
<body>

  <section class="card-back" aria-label="Business card back">
    <div class="card-back__mark"></div>
    <div class="card-back__name">Bramble<br>Travel Planners</div>
  </section>

  <section class="card-front" aria-label="Business card front">
    <svg class="card-front__waves" viewBox="0 0 640 366" preserveAspectRatio="none" aria-hidden="true">
      <path d="M90,10 C60,80 90,150 170,170" fill="none" stroke="#8cc63f" stroke-width="10" stroke-linecap="round"/>
      <path d="M0,110 C150,250 380,205 640,215 L640,366 L0,366 Z" fill="#1d7fae"/>
      <path d="M240,196 C400,201 540,210 640,213 L640,236 C520,228 400,216 240,196 Z" fill="#0e4a7d"/>
      <path d="M0,366 L0,270 C150,335 400,345 640,335 L640,366 Z" fill="#135e8e" opacity="0.6"/>
    </svg>
    <div class="card-front__mark"></div>
    <div class="card-front__name">Bramble Travel Planners</div>

    <div class="contact">
      <div class="contact__person">Warren Pelfrey</div>
      <div class="contact__role">Owner</div>
      <div class="contact__line">(555) 014-2287
        <svg class="contact__icon" viewBox="0 0 16 16" aria-hidden="true"><circle cx="8" cy="8" r="8" fill="#8cc63f"/><path d="M5 4 L7 4 L7.5 6 L6.5 7 C7 8.2 7.8 9 9 9.5 L10 8.5 L12 9 L12 11 C8 11.5 4.5 8 5 4 Z" fill="#135e8e"/></svg>
      </div>
      <div class="contact__line">BrambleTravelPlanners.com
        <svg class="contact__icon" viewBox="0 0 16 16" aria-hidden="true"><circle cx="8" cy="8" r="8" fill="#8cc63f"/><circle cx="8" cy="8" r="4.5" fill="none" stroke="#135e8e" stroke-width="1.2"/><path d="M3.5 8 H12.5 M8 3.5 V12.5" stroke="#135e8e" stroke-width="1.2"/></svg>
      </div>
      <div class="contact__line">WPelfrey@BrambleTravelPlanners.com
        <svg class="contact__icon" viewBox="0 0 16 16" aria-hidden="true"><circle cx="8" cy="8" r="8" fill="#8cc63f"/><rect x="4" y="5" width="8" height="6" fill="none" stroke="#135e8e" stroke-width="1.2"/><path d="M4 5 L8 8.5 L12 5" fill="none" stroke="#135e8e" stroke-width="1.2"/></svg>
      </div>
    </div>
  </section>

  <div class="brand-logo">
    <div class="brand-logo__mark"></div>
    <div class="brand-logo__name">Bramble Travel Planners</div>
  </div>

</body>
</html>
```